Loan Company looking to offer special summer loan rate for closed customers

We are wanting to design an A5 Summer Holiday themed leaflet. We would like to offer a 10% Cashback when re-opening their loan account.
The leaflet is aimed at our closed customers. We would like to use bright summer colours. I have uploaded one of our Christmas promotion leaflets for you to include the highlighted information to use in this new project. We have also uploaded some ideas of examples that we have seen online as rough guide.
"10% Cashback on all re-opened accounts in July and August 2023!"

```html
<!DOCTYPE html>
<html lang="en">
<head>
<meta charset="utf-8">
<title>Marlow Lending – Summer Cashback Leaflet</title>
<link rel="stylesheet" href="https://fonts.googleapis.com/css2?family=Bebas+Neue&family=Montserrat:wght@400;500;600&display=swap">
<style>
  :root {
    --page-bg: #f1f1f2;
    --teal-deep: #0a6e7e;
    --teal-mid: #11a9bf;
    --teal-pale: #cfe9ee;
    --teal-mist: #bfe0e8;
    --brush-light: #c9dba6;
    --brush-mid: #4f8a6a;
    --brush-dark: #1f4a42;
    --orange: #f6a640;
    --orange-deep: #f39a2b;
    --green-bar-top: #4d8666;
    --green-bar-bottom: #24443d;
    --ink: #1b1b1b;
    --white: #ffffff;
    --url-teal: #1d6470;
  }
  * { box-sizing: border-box; margin: 0; padding: 0; }
  html, body {
    width: 917px; height: 1200px; overflow: hidden;
    background: var(--page-bg);
  }
  .leaflet {
    position: absolute; left: 83px; top: 20px;
    width: 751px; height: 1160px; overflow: hidden;
    font-family: "Montserrat", Arial, sans-serif;
    color: var(--ink);
  }
  .beach-backdrop {
    position: absolute; inset: 0;
    background: linear-gradient(180deg, var(--teal-deep) 0%, var(--teal-mid) 22%, #5cc6d4 42%, var(--teal-pale) 68%, var(--teal-mist) 100%);
  }
  .brand { position: absolute; top: 50px; left: 0; right: 0; text-align: center; color: var(--white); }
  .brand-name { font-weight: 500; font-size: 72px; line-height: 1; letter-spacing: 1px; }
  .brand-sub { font-weight: 500; font-size: 15px; margin-top: 2px; }
  .offer-brush {
    position: absolute; left: 145px; top: 202px; width: 460px; height: 474px;
    background: linear-gradient(170deg, var(--brush-light) 0%, #8fb386 30%, var(--brush-mid) 60%, var(--brush-dark) 100%);
    border-radius: 6px;
  }
  .offer-frame {
    position: absolute; left: 218px; top: 246px; width: 323px; height: 395px;
    border: 4px solid var(--white);
  }
  .offer-figure, .offer-word, .offer-period {
    position: absolute; left: 0; right: 0; text-align: center; white-space: nowrap;
    font-family: "Bebas Neue", Impact, sans-serif; color: var(--white); line-height: 1;
  }
  .offer-figure { top: 279px; font-size: 214px; }
  .offer-word { top: 460px; font-size: 78px; }
  .offer-pill {
    position: absolute; left: 242px; top: 537px; width: 280px; height: 31px;
    border-radius: 16px; background: var(--orange);
    color: var(--white); font-size: 17px; font-weight: 500; white-space: nowrap;
    display: flex; align-items: center; justify-content: center;
  }
  .offer-period { top: 573px; font-size: 38px; transform: scaleX(0.88); }
  .terms { position: absolute; left: 0; right: 0; text-align: center; font-size: 15.5px; line-height: 21px; white-space: nowrap; }
  .terms-example { top: 746px; }
  .terms-rate { top: 808px; }
  .terms-legal { top: 899px; font-size: 14px; line-height: 19px; }
  .terms-legal strong { font-weight: 600; }
  .contact-bar {
    position: absolute; left: 108px; top: 987px; width: 534px; height: 73px; display: flex;
  }
  .contact-label {
    width: 198px; flex: none; background: linear-gradient(180deg, var(--green-bar-top), var(--green-bar-bottom));
    color: var(--white); font-family: "Bebas Neue", Impact, sans-serif; white-space: nowrap;
    font-size: 25px; line-height: 23px; padding: 14px 0 0 17px;
  }
  .contact-phone {
    flex: 1; background: linear-gradient(180deg, #f9b85c, var(--orange-deep));
    color: var(--white); font-family: "Bebas Neue", Impact, sans-serif; white-space: nowrap;
    font-size: 66px; line-height: 75px; text-align: center;
  }
  .web-strip {
    position: absolute; left: 134px; top: 1100px; width: 483px; height: 34px;
    background: var(--white); border-radius: 3px 14px 3px 14px;
    display: flex; align-items: center; justify-content: center; white-space: nowrap;
    font-family: "Bebas Neue", Impact, sans-serif; font-size: 19px;
    letter-spacing: 5px; color: var(--url-teal);
  }
</style>
</head>
<body>
  <main class="leaflet">
    <div class="beach-backdrop" role="img" aria-label="Misty tropical beach with palm trees and sun loungers"></div>

    <header class="brand">
      <div class="brand-name">MARLOW</div>
      <div class="brand-sub">LENDING SERVICES (YORKSHIRE) LIMITED</div>
    </header>

    <div class="offer-brush" role="img" aria-label="Green brush-stroke paint swatch behind the offer"></div>
    <div class="offer-frame"></div>
    <div class="offer-figure">10%</div>
    <div class="offer-word">CASHBACK</div>
    <div class="offer-pill">on all re-opened accounts</div>
    <div class="offer-period">IN JULY AND AUGUST 2023!</div>

    <p class="terms terms-example">Representative example: Loan amount $150.00 payable over 23<br>weeks at $10.50 per week.</p>
    <p class="terms terms-rate">interest is $91.50 THe Total amount payable is $241.50. Interest<br>rate is 138.29% per annum (fixed). 838.39% APR representative.</p>
    <p class="terms terms-legal"><strong>Term and Conditions apply.</strong><br>All credit is Subject to status &amp; affordability.<br>Written quotations on request</p>

    <div class="contact-bar">
      <div class="contact-label">FOR MORE INFORMATION<br>CONTACT OUR OFFICE ON</div>
      <div class="contact-phone">01632 960 415</div>
    </div>

    <div class="web-strip">WWW.MARLOWLENDING.COM</div>
  </main>
</body>
</html>
```